Inspire Design with Natural Stone: Quarrelle Inc. Tradeshow Booth Backdrop

Client: Quarrelle Inc.
Project Goal: To design a visually compelling and informative 7.5ft x 10ft backdrop for Quarrelle Inc.'s 10ft x 10ft tradeshow booth that attracts and engages architects, designers, homeowners, and contractors, ultimately driving interest in their natural stone products.
Quarrelle Inc. is a leading provider of high-quality natural stone for a wide range of residential and commercial projects. We offer a diverse selection of stone types, finishes, and applications, known for their beauty, durability, and timeless appeal. We are participating in upcoming tradeshows to generate new leads, strengthen brand awareness, and showcase our latest offerings to key target audiences.
Target Audience(s):
Architects: Seeking premium, unique, and sustainable natural stone options for their designs, with an appreciation for quality and aesthetic integration.
Designers (Interior & Landscape): Looking for visually appealing and versatile stone to enhance their projects, focusing on texture, color palettes, and application possibilities.
Homeowners: Aspiring to elevate their living spaces with natural stone, driven by aesthetics, durability, and adding lasting value to their homes.
Contractors: Seeking reliable and high-quality stone suppliers for their building and renovation projects, prioritizing ease of installation and client satisfaction.
Key Message/Desired Outcome: We want our booth to communicate that Quarrelle Inc. is the premier source for beautiful, high-quality natural stone solutions for any project, backed by expertise and a commitment to customer satisfaction. We want to inspire visitors with the possibilities of using natural stone in their designs and projects.
Mandatories:
* Backdrop Dimensions: 7.5 feet (height) x 10 feet (width). (See attached template)
* Inclusion of Quarrelle Inc. Logo:* The logo must be prominently featured and easily recognizable. Please refer to the attached brand guidelines for logo usage, color palette, and typography.
*Clear Representation of Natural Stone: The design must showcase the beauty and variety of Quarrelle Inc.'s natural stone products. This can be achieved through high-quality photography, subtle textures, or artistic representations. Please use our website's photo and project gallery.
*Contact Information: Include our website address: www.quarrelle-example.com
Optional Elements (Consideration):
*Visuals of Applications: Showcasing natural stone used in various settings (e.g., fireplaces, facades, patios, interior walls) could be impactful.
*Highlighting Key Benefits: Briefly communicating the advantages of natural stone (e.g., durability, sustainability, timelessness).
*Integration of Textures: Subtly incorporating textures that hint at the feel of natural stone.
Look and Feel:
*Overall Impression: Sophisticated, natural, high-quality, inviting, trustworthy, and inspiring.
*Style: Clean, modern, and visually appealing, allowing the beauty of the stone to take center stage. Avoid overly busy or cluttered designs.
*Color Palette: Primarily utilize Quarrelle Inc.'s brand colors (refer to brand guidelines).
Things to Avoid:
* Generic stock imagery that doesn't accurately represent Quarrelle's products.
* Cluttered layouts with excessive text.
* Designs that appear cheap or unprofessional.
* Difficult-to-read fonts or color combinations.
Deliverables:
* High-resolution digital design file(s) suitable for large-format printing (AI, Photoshop, PDF).
* Mockup of the backdrop design within a 10ft x 10ft booth space. Please feel free to include any other booth features (tables, flooring, etc) that you think would work well with the backdrop (optional but highly recommended).
We are excited to see your creative interpretations and look forward to selecting a design that will make a strong and lasting impression at our upcoming tradeshows!

```html
<!DOCTYPE html>
<html lang="en">
<head>
<meta charset="utf-8">
<title>Quarrelle Inc. Tradeshow Backdrop</title>
<link href="https://fonts.googleapis.com/css2?family=Exo+2:wght@300;400;500;600;700&display=swap" rel="stylesheet">
<style>
  :root {
    --page-bg: #3a3e4a;
    --navy: #111c2b;
    --slate: #7c7d80;
    --title-grey: #6d6e72;
    --text: #1c2430;
    --marble-light: #f6f6f7;
    --marble-mid: #e4e4e7;
    --line: #1c2430;
    --white: #ffffff;
  }
  * { box-sizing: border-box; margin: 0; padding: 0; }
  html, body { width: 1200px; height: 2179px; overflow: hidden; }
  body {
    background: var(--page-bg);
    font-family: "Exo 2", sans-serif;
    color: var(--text);
    position: relative;
  }
  .backdrop {
    position: absolute;
    left: 50px; top: 678px;
    width: 1100px; height: 823px;
    background:
      linear-gradient(125deg, rgba(255,255,255,0) 20%, rgba(210,210,216,0.45) 32%, rgba(255,255,255,0) 42%),
      linear-gradient(140deg, rgba(255,255,255,0) 60%, rgba(205,205,212,0.4) 72%, rgba(255,255,255,0) 82%),
      linear-gradient(160deg, var(--marble-light) 0%, var(--marble-mid) 55%, var(--marble-light) 100%);
    box-shadow: 0 14px 30px rgba(0,0,0,0.45);
    overflow: hidden;
  }
  .headline { position: absolute; right: 666px; top: 76px; text-align: right; }
  .headline-kicker {
    font-weight: 300; font-size: 33px; color: var(--title-grey);
    line-height: 1; letter-spacing: 0.5px;
  }
  .headline-main {
    font-weight: 700; font-size: 46px; color: var(--navy);
    line-height: 1; margin-top: 5px; letter-spacing: 0.5px; white-space: nowrap;
  }
  .intro {
    position: absolute; right: 668px; top: 176px; width: 400px;
    text-align: right; font-size: 15.5px; line-height: 1.25; color: var(--text);
  }
  .frame-line { position: absolute; background: var(--line); }
  .photo { position: absolute; }
  .photo-fireplace-rustic {
    left: 675px; top: 99px; width: 229px; height: 322px;
    background: linear-gradient(180deg, #6b5a45 0%, #a69883 35%, #8e7f69 70%, #7a4f2a 100%);
  }
  .photo-wall-garden {
    left: 439px; top: 361px; width: 229px; height: 323px;
    background: linear-gradient(180deg, #5b6f4a 0%, #7d8a66 40%, #a8a394 62%, #4a4a4c 100%);
  }
  .photo-fireplace-slate {
    left: 202px; top: 268px; width: 229px; height: 322px;
    background: linear-gradient(90deg, #d9d6d1 0%, #b9b5ae 40%, #56585b 55%, #4a4c50 75%, #8a6e4e 100%);
  }
  .brand-name {
    position: absolute; left: 439px; top: 290px; width: 229px;
    text-align: center; font-weight: 600; font-size: 30px;
    color: var(--navy); letter-spacing: 1px;
  }
  .offer-heading {
    position: absolute; left: 689px; top: 450px;
    font-weight: 600; font-size: 17.5px; line-height: 1.2; color: var(--navy);
  }
  .offer-list { position: absolute; left: 675px; top: 504px; width: 245px; list-style: none; }
  .offer-item {
    height: 28px; margin-bottom: 2.5px; display: flex; align-items: center;
    padding-left: 30px; font-size: 16px; color: var(--white); font-weight: 500;
  }
  .offer-item svg { width: 12px; height: 12px; margin-right: 8px; flex: none; }
  .offer-item--dark { background: var(--navy); }
  .offer-item--grey { background: var(--slate); }
  .website {
    position: absolute; left: 0; right: 0; top: 738px; text-align: center;
    font-size: 24px; letter-spacing: 14px; color: var(--navy); font-weight: 300;
  }
  .website strong { font-weight: 700; }
</style>
</head>
<body>
  <section class="backdrop">
    <div class="headline">
      <div class="headline-kicker">CRAFT YOUR</div>
      <div class="headline-main">VISION IN STONE</div>
    </div>
    <p class="intro">Quarrelle Inc. is a leading provider of high-quality natural stone for a wide range of residential and commercial projects.</p>

    <div class="frame-line" style="left:448px; top:80px; width:474px; height:1.5px;"></div>
    <div class="frame-line" style="left:920px; top:80px; width:1.5px; height:230px;"></div>
    <div class="frame-line" style="left:187px; top:374px; width:1.5px; height:232px;"></div>
    <div class="frame-line" style="left:187px; top:605px; width:230px; height:1.5px;"></div>

    <div class="photo photo-fireplace-rustic" role="img" aria-label="Photo of a tall natural fieldstone fireplace in a wood-beamed living room"></div>
    <div class="photo photo-fireplace-slate" role="img" aria-label="Photo of a dark grey stone-clad fireplace column in a high-ceiling living room"></div>
    <div class="photo photo-wall-garden" role="img" aria-label="Photo of a dry-stacked natural stone garden wall beside a house"></div>

    <div class="brand-name">QUARRELLE</div>

    <h3 class="offer-heading">We offer a diverse<br>selection of</h3>
    <ul class="offer-list">
      <li class="offer-item offer-item--dark"><svg viewBox="0 0 12 12"><circle cx="6" cy="6" r="6" fill="#c9c9cc"/><path d="M3.3 6.2l1.8 1.8 3.6-3.7" stroke="#111c2b" stroke-width="1.5" fill="none"/></svg>Stone types</li>
      <li class="offer-item offer-item--grey"><svg viewBox="0 0 12 12"><circle cx="6" cy="6" r="6" fill="#c9c9cc"/><path d="M3.3 6.2l1.8 1.8 3.6-3.7" stroke="#7c7d80" stroke-width="1.5" fill="none"/></svg>Finishes</li>
      <li class="offer-item offer-item--dark"><svg viewBox="0 0 12 12"><circle cx="6" cy="6" r="6" fill="#c9c9cc"/><path d="M3.3 6.2l1.8 1.8 3.6-3.7" stroke="#111c2b" stroke-width="1.5" fill="none"/></svg>Applications</li>
      <li class="offer-item offer-item--grey"><svg viewBox="0 0 12 12"><circle cx="6" cy="6" r="6" fill="#c9c9cc"/><path d="M3.3 6.2l1.8 1.8 3.6-3.7" stroke="#7c7d80" stroke-width="1.5" fill="none"/></svg>Known for their beauty</li>
      <li class="offer-item offer-item--dark"><svg viewBox="0 0 12 12"><circle cx="6" cy="6" r="6" fill="#c9c9cc"/><path d="M3.3 6.2l1.8 1.8 3.6-3.7" stroke="#111c2b" stroke-width="1.5" fill="none"/></svg>Durability</li>
      <li class="offer-item offer-item--grey"><svg viewBox="0 0 12 12"><circle cx="6" cy="6" r="6" fill="#c9c9cc"/><path d="M3.3 6.2l1.8 1.8 3.6-3.7" stroke="#7c7d80" stroke-width="1.5" fill="none"/></svg>Timeless appeal</li>
    </ul>

    <div class="website">www.<strong>quarrelle-example</strong>.com</div>
  </section>
</body>
</html>
```